Real Estate Card Design

I need a new business card! Below you will find my headshot, the company logo and a copy of my previous business card.

The card must contain the following information:

Dana Welch
Sales Representative
FAIR HARBOUR HOMES REALTY INC BROKERGE
204-517 Maple Ave E, Oshawa ON L1G 4K7
Cell: 905-618-4037 Office:905-481-2696
www.danawelch.com dana@movewithwelch.ca

I would like the card to portray security and class all the while being fresh and contemporary. I hold the key....

```html
<!DOCTYPE html>
<html lang="en">
<head>
<meta charset="utf-8">
<title>Dana Welch – Business Card</title>
<link rel="stylesheet" href="https://fonts.googleapis.com/css2?family=Tinos:wght@400;700&display=swap">
<style>
  :root {
    --brand-blue: #00a3e4;
    --ink: #111111;
    --paper: #ffffff;
    --portrait-dark: #1b1d1f;
    --portrait-mid: #2c2f33;
  }
  html, body {
    margin: 0;
    padding: 0;
    width: 1200px;
    height: 686px;
    overflow: hidden;
    background: var(--paper);
  }
  .card {
    position: relative;
    width: 1200px;
    height: 686px;
    background: var(--paper);
    overflow: hidden;
    font-family: "Tinos", "Times New Roman", serif;
    color: var(--ink);
  }
  .card__art {
    position: absolute;
    inset: 0;
    width: 1200px;
    height: 686px;
  }
  .brand {
    position: absolute;
    left: 66px;
    top: 62px;
    display: flex;
    align-items: center;
    gap: 16px;
  }
  .brand__square {
    width: 58px;
    height: 58px;
    background: var(--brand-blue);
    flex: none;
  }
  .brand__name {
    margin: 0;
    font-size: 24px;
    font-weight: 700;
    line-height: 1.12;
    letter-spacing: 0.5px;
    color: var(--ink);
  }
  .agent {
    position: absolute;
    left: 62px;
    top: 282px;
  }
  .agent__name {
    margin: 0;
    font-size: 47px;
    font-weight: 400;
    line-height: 1;
    color: var(--brand-blue);
  }
  .agent__title {
    margin: 10px 0 0;
    font-size: 22px;
    font-weight: 400;
  }
  .contact {
    position: absolute;
    left: 60px;
    top: 410px;
    margin: 0;
    padding: 0;
    list-style: none;
  }
  .contact__item {
    display: flex;
    align-items: center;
    height: 48px;
    font-size: 22px;
  }
  .contact__icon {
    width: 34px;
    height: 34px;
    margin-right: 28px;
    flex: none;
    fill: var(--ink);
  }
</style>
</head>
<body>
<main class="card">
  <svg class="card__art" viewBox="0 0 1050 600" preserveAspectRatio="none" aria-hidden="false">
    <defs>
      <radialGradient id="portraitTone" cx="0.45" cy="0.45" r="0.7">
        <stop offset="0" stop-color="var(--portrait-mid)"/>
        <stop offset="1" stop-color="var(--portrait-dark)"/>
      </radialGradient>
    </defs>
    <path class="card__swoosh" d="M425 600 C520 560 600 420 645 232 L700 232 L760 600 Z" fill="var(--brand-blue)"/>
    <circle class="card__ring" cx="940" cy="290" r="318" fill="var(--paper)"/>
    <circle class="card__portrait" cx="940" cy="290" r="305" fill="url(#portraitTone)" role="img" aria-label="Portrait of the agent in a pinstripe suit holding up a house key"/>
  </svg>

  <div class="brand">
    <span class="brand__square"></span>
    <p class="brand__name">FAIR HARBOUR HOMES<br>REALTY INC<br>BROKERGE</p>
  </div>

  <section class="agent">
    <h1 class="agent__name">Dana Welch</h1>
    <p class="agent__title">Sales Representative</p>
  </section>

  <ul class="contact">
    <li class="contact__item">
      <svg class="contact__icon" viewBox="0 0 24 24"><path d="M12 1.5a7.5 7.5 0 0 0-7.5 7.5c0 5.6 7.5 13.5 7.5 13.5s7.5-7.9 7.5-13.5A7.5 7.5 0 0 0 12 1.5zm0 10.6a3.1 3.1 0 1 1 0-6.2 3.1 3.1 0 0 1 0 6.2z"/></svg>
      204-517 Maple Ave E, Oshawa ON L1G 4K7
    </li>
    <li class="contact__item">
      <svg class="contact__icon" viewBox="0 0 24 24"><path d="M6.6 2.5 9.4 6.2 7.6 8.6c1.2 2.8 3.2 4.9 6 6.1l2.3-1.8 3.7 2.8-1.6 4.3C10.6 19.8 4 13.2 3.7 5.1z"/><path d="M13.5 2.5a8 8 0 0 1 8 8h-1.8a6.2 6.2 0 0 0-6.2-6.2z M13.5 6a4.5 4.5 0 0 1 4.5 4.5h-1.8a2.7 2.7 0 0 0-2.7-2.7z"/></svg>
      905-481-2696
    </li>
    <li class="contact__item">
      <svg class="contact__icon" viewBox="0 0 24 24"><path d="M8 1h8a2 2 0 0 1 2 2v18a2 2 0 0 1-2 2H8a2 2 0 0 1-2-2V3a2 2 0 0 1 2-2zm0 3v14h8V4zm4 15.5a1 1 0 1 0 0 2 1 1 0 0 0 0-2z"/></svg>
      905-618-4037
    </li>
    <li class="contact__item">
      <svg class="contact__icon" viewBox="0 0 24 24"><path d="M1 5h22v14H1zm2 2v.3l9 6 9-6V7zm0 2.7V17h18V9.7l-9 6z"/></svg>
      dana@movewithwelch.ca
    </li>
    <li class="contact__item">
      <svg class="contact__icon" viewBox="0 0 24 24"><path d="M12 1a11 11 0 1 0 0 22 11 11 0 0 0 0-22zm7.9 10h-3.5a17 17 0 0 0-1.3-6.9A9 9 0 0 1 19.9 11zM12 3.1c1 1.3 2.2 4 2.4 7.9H9.6C9.8 7.1 11 4.4 12 3.1zM8.9 4.1A17 17 0 0 0 7.6 11H4.1a9 9 0 0 1 4.8-6.9zM4.1 13h3.5a17 17 0 0 0 1.3 6.9A9 9 0 0 1 4.1 13zm7.9 7.9c-1-1.3-2.2-4-2.4-7.9h4.8c-.2 3.9-1.4 6.6-2.4 7.9zm3.1-1A17 17 0 0 0 16.4 13h3.5a9 9 0 0 1-4.8 6.9z"/></svg>
      www.danawelch.com
    </li>
  </ul>
</main>
</body>
</html>
```